Spa Business Card Design Project

Hello! We are a boutique spa for men and women that is rebranding. I would like a memorable new business card that showcases our beautiful new logo and our unique business. I would like it to be classic/timeless and eclectic/artistic at the  same time.
I am a fan of negative space as you can tell from the logo. I am also open to any creative ideas.
Multi sided design. Two sided design is acceptable as an option, too. "Flaps/folds/whatever the design term is" are optional- whether full vertical or horizontal, half flap, full flap etc
On either side next to the golden snail I would potentially like to see "slow down. Enjoy Life."  Possibly on one statment on top of each other, crowned with the snail. Or the statment following the snail on one line... I am open for a creative suprise, too.
The back I would like room for the standard Information
"3817 Birch Lane
Fernhollow, New York 10999
(555) 462 3085
info@thecorvella spa.com
The snail is to be done in gold ink.
Can I also Have an option for cards that are individualized for staff members, too?

Updates
Project Deadline Extended
Reason: I apologize for the deadline extension. My day was more involved than anticipated in other matters. Hope to have this closed by next Tuesday.
Thank you

Target Market(s)
Men and women with expendable income between the ages of 30-55
Industry/Entity Type
Boutique
Requirements
Must have
- only black and gold ink.

Nice to have
- One of a kind.
Showcase the snail :-)
make you smile :-)
Fun, but professional.
Should not have
- Lots of color.
Too feminine.
Too busy.

```html
<!DOCTYPE html>
<html lang="en">
<head>
<meta charset="utf-8">
<title>The Corvella Spa — Business Card</title>
<link rel="stylesheet" href="https://fonts.googleapis.com/css2?family=Cormorant+Garamond:wght@400;500&family=Raleway:wght@300;400;600&display=swap">
<style>
  :root {
    --stage: #d9d9d7;
    --paper: #ffffff;
    --ink: #2b2b2b;
    --ink-soft: #8a8a8a;
    --gold: #c9a25c;
    --gold-light: #e0c48a;
    --black-top: #1b1b1b;
    --black-bottom: #050505;
  }
  * { box-sizing: border-box; margin: 0; padding: 0; }
  html, body {
    width: 1200px;
    height: 900px;
    overflow: hidden;
    background: var(--stage);
  }
  .canvas {
    width: 1200px;
    height: 900px;
    display: flex;
    justify-content: center;
    align-items: center;
    gap: 60px;
  }
  .card {
    position: relative;
    width: 360px;
    height: 630px;
    box-shadow: 0 10px 30px rgba(0,0,0,0.18);
  }
  .card__frame {
    position: absolute;
    inset: 14px;
    border: 1.5px solid var(--gold-light);
  }

  /* Front */
  .card--front { background: var(--paper); }
  .wordmark {
    position: absolute;
    top: 40px;
    left: 0;
    right: 0;
    text-align: center;
    font-family: "Cormorant Garamond", serif;
    font-weight: 500;
    font-size: 40px;
    line-height: 1.05;
    color: var(--ink);
  }
  .wordmark__tagline {
    display: block;
    margin-top: 10px;
    font-family: "Raleway", sans-serif;
    font-weight: 400;
    font-size: 13px;
    color: var(--ink);
  }
  .staff {
    position: absolute;
    top: 268px;
    left: 0;
    right: 0;
    text-align: center;
  }
  .staff__name {
    font-family: "Raleway", sans-serif;
    font-weight: 400;
    font-size: 30px;
    color: var(--gold);
  }
  .staff__role {
    margin-top: 4px;
    font-family: "Cormorant Garamond", serif;
    font-size: 17px;
    color: var(--ink);
  }
  .contact {
    position: absolute;
    right: 36px;
    top: 430px;
    text-align right;
    text-align: right;
    font-style: normal;
    font-family: "Raleway", sans-serif;
    font-weight: 300;
    font-size: 13px;
    line-height: 1.55;
    color: var(--ink-soft);
  }
  .contact__gap { margin-top: 12px; }
  .contact__label { font-weight: 600; color: var(--ink); }
  .contact__web {
    margin-top: 16px;
    font-weight: 600;
    color: var(--gold);
  }

  /* Back */
  .card--back {
    background: linear-gradient(180deg, var(--black-top), var(--black-bottom));
  }
  .card--back .card__frame { border-color: var(--gold); }
  .emblem {
    position: absolute;
    top: 262px;
    left: 50%;
    width: 92px;
    height: 60px;
    margin-left: -46px;
    border-radius: 30px 30px 8px 8px;
    background: var(--gold);
  }
  .motto {
    position: absolute;
    top: 336px;
    left: 0;
    right: 0;
    text-align: center;
    font-family: "Raleway", sans-serif;
    font-weight: 400;
    font-size: 21px;
    color: var(--gold);
  }
</style>
</head>
<body>
  <main class="canvas">
    <section class="card card--front">
      <div class="card__frame"></div>
      <h1 class="wordmark">The Corvella Spa
        <span class="wordmark__tagline">a boutique spa for Men &amp; Women</span>
      </h1>
      <div class="staff">
        <p class="staff__name">Name Here</p>
        <p class="staff__role">beauty therapist</p>
      </div>
      <address class="contact">
        <p>3817 Birch Lane</p>
        <p>Fernhollow, New York 10999</p>
        <p class="contact__gap"><span class="contact__label">T:</span> (555) 462 3085</p>
        <p><span class="contact__label">E:</span> info@thecorvella spa.com</p>
        <p class="contact__web">www.thecorvellaspa.com</p>
      </address>
    </section>

    <section class="card card--back">
      <div class="card__frame"></div>
      <div class="emblem" role="img" aria-label="Gold snail illustration"></div>
      <p class="motto">slow down. enjoy life.</p>
    </section>
  </main>
</body>
</html>
```